Natural Health Practice Postcard Marketing

I'm a Traditional Naturopath and provide natural health consulting services and I call my company Marigold Health. My target audience are women ages 35 - 65 and I focus on hormone issues, digestion, kidney disorders and chronic health conditions. The focus is try to make it clear why someone would contact me, essentially what conditions I work with and maybe some questions (e.g. are you tired of taking prescription drugs', identify root cause, etc). I would like a new postcard (have attached the old one) which references to natural health vs. naturopathy (as most folks don't know what that is). Also for reference is my website www.marigold-health.example

35 - 65 year old women with hormone issues, chronic conditions, digestive or kidney issues.

• language on both sides of card and no need for return address as not mailing postcard just using for marketing materials
• consistent with look/feel of website
• not sending a postcard so return address / postage location not needed

```html
<!DOCTYPE html>
<html lang="en">
<head>
<meta charset="utf-8">
<title>Marigold Health Postcard</title>
<link rel="stylesheet" href="https://fonts.googleapis.com/css2?family=EB+Garamond:wght@400;600;700&display=swap">
<style>
  :root {
    --page-bg: #e6e6e4;
    --leaf-green: #6aa83a;
    --deep-green: #4f8a2c;
    --band-green: #5f9434;
    --cream: #f6f8e0;
    --pale-green: #e8efd0;
    --stripe-grey: #a9a592;
    --ink-olive: #4f4a2e;
    --ink-body: #3e3d32;
    --accent-green: #5c9432;
    --brand-blue: #3a5a8c;
    --white: #ffffff;
  }
  * { margin: 0; padding: 0; box-sizing: border-box; }
  html, body { width: 900px; height: 1200px; overflow: hidden; }
  body {
    background: var(--page-bg);
    font-family: "EB Garamond", Georgia, serif;
    color: var(--ink-body);
    position: relative;
  }
  .card {
    position: absolute;
    left: 110px;
    width: 680px;
    overflow: hidden;
    box-shadow: 0 2px 8px rgba(0,0,0,0.18);
  }
  .card-front { top: 40px; height: 545px; background: var(--cream); }
  .card-back { top: 630px; height: 510px; background: var(--cream); }
  .card-shapes { position: absolute; inset: 0; }

  /* front */
  .front-questions {
    position: absolute;
    right: 26px;
    top: 48px;
    width: 340px;
    text-align: right;
    font-size: 18.5px;
    line-height: 25px;
    color: var(--ink-olive);
  }
  .front-questions p { margin-bottom: 13px; }
  .highlight { color: var(--accent-green); font-weight: 700; }
  .practitioner {
    position: absolute;
    right: 26px;
    top: 373px;
    font-size: 21px;
    font-weight: 700;
    color: var(--ink-olive);
  }
  .brand {
    position: absolute;
    left: 30px;
    top: 470px;
    display: flex;
    align-items: center;
    gap: 10px;
  }
  .brand-dot {
    width: 22px; height: 22px;
    border-radius: 50%;
    background: var(--leaf-green);
  }
  .brand-name {
    font-size: 26px;
    color: var(--brand-blue);
    font-weight: 400;
  }
  .tagline {
    position: absolute;
    left: 232px;
    top: 470px;
    font-size: 25px;
    color: var(--ink-olive);
  }

  /* back */
  .back-intro {
    position: absolute;
    left: 22px;
    top: 22px;
    width: 340px;
    font-size: 17.5px;
    line-height: 23px;
    color: var(--ink-body);
  }
  .back-intro p { margin-bottom: 13px; }
  .photo { position: absolute; }
  .photo-herbs {
    left: 22px; top: 298px; width: 232px; height: 165px;
    background: linear-gradient(135deg, #7f9a5a 0%, #d9d3bf 45%, #8a6a3e 75%, #e8e2cf 100%);
  }
  .conditions {
    position: absolute;
    right: 30px;
    top: 308px;
    text-align: right;
    font-size: 17.5px;
    line-height: 23px;
    color: var(--ink-body);
  }
  .conditions-list { list-style: none; margin-top: 16px; line-height: 25px; }
  .contact-bar {
    position: absolute;
    left: 0; right: 0; bottom: 0;
    height: 42px;
    background: var(--band-green);
    color: var(--white);
    font-size: 18px;
    display: flex;
    align-items: center;
    justify-content: center;
  }
  .contact-bar strong { font-weight: 700; margin: 0 5px; }
</style>
</head>
<body>

<section class="card card-front" aria-label="Postcard front">
  <svg class="card-shapes" width="680" height="545" viewBox="0 0 680 545">
    <defs>
      <radialGradient id="leafGlow" cx="0.4" cy="0.4" r="0.8">
        <stop offset="0" stop-color="#a9d160"/>
        <stop offset="0.5" stop-color="#6aa83a"/>
        <stop offset="1" stop-color="#3f7d26"/>
      </radialGradient>
      <linearGradient id="creamFade" x1="0" y1="0" x2="1" y2="1">
        <stop offset="0" stop-color="#fbfcf0"/>
        <stop offset="1" stop-color="#eef3d2"/>
      </linearGradient>
    </defs>
    <rect width="680" height="545" fill="url(#creamFade)"/>
    <path class="curve-stripe" d="M0 0 H352 C300 130 240 300 0 402 Z" fill="var(--stripe-grey)"/>
    <g role="img" aria-label="Photo of ginkgo leaves on a soft green background">
      <path d="M0 0 H335 C285 130 225 290 0 392 Z" fill="url(#leafGlow)"/>
    </g>
    <path class="wave-band" d="M0 388 C200 392 450 420 680 452 V545 H0 Z" fill="var(--band-green)"/>
    <path class="footer-white" d="M0 404 C200 406 450 432 680 470 V545 H0 Z" fill="var(--white)"/>
  </svg>

  <div class="front-questions">
    <p>Tired of taking prescription drugs or worried about the side effects?</p>
    <p>Trying to identify the root cause of your health problem?</p>
    <p>Worried about an illness that runs in your family or just looking for ways to stay healthy?</p>
    <p><span class="highlight">Natural health</span> can be used to support all health conditions, from wellness and prevention to acute and chronic health issues.</p>
  </div>
  <div class="practitioner">Clara Bennett, Traditional Naturopath</div>

  <div class="brand">
    <span class="brand-dot"></span>
    <span class="brand-name">Marigold Health</span>
  </div>
  <div class="tagline" style="left:262px">Take control of your health - naturally.</div>
</section>

<section class="card card-back" aria-label="Postcard back">
  <svg class="card-shapes" width="680" height="510" viewBox="0 0 680 510">
    <defs>
      <linearGradient id="meadow" x1="0" y1="0" x2="0" y2="1">
        <stop offset="0" stop-color="#b8d48a"/>
        <stop offset="0.45" stop-color="#7fb04a"/>
        <stop offset="1" stop-color="#e7eed8"/>
      </linearGradient>
    </defs>
    <rect width="680" height="510" fill="var(--cream)"/>
    <path class="swoosh" d="M355 0 C400 120 330 250 400 510 H680 V0 Z" fill="var(--pale-green)"/>
    <path class="photo-frame" d="M372 0 H680 V272 H410 C375 200 395 90 372 0 Z" fill="var(--white)"/>
    <g role="img" aria-label="Photo of a woman in a white dress with arms outstretched in a sunny meadow">
      <path d="M380 8 H680 V264 H416 C384 195 402 92 380 8 Z" fill="url(#meadow)"/>
    </g>
  </svg>

  <div class="back-intro">
    <p><span class="highlight">Natural health</span> as practiced by Traditional Naturopaths provides an alternative approach to conventional medicine.</p>
    <p>The objective of natural health is to harness the <span class="highlight">body's ability to heal itself</span> with the support of <span class="highlight">natural remedies</span> like foods, vitamins / minerals, herbs, essential oils, homeopathics / cell salts or flower essences.</p>
  </div>

  <div class="photo photo-herbs" role="img" aria-label="Photo of fresh herbs, a mortar, dropper bottles and supplement capsules"></div>

  <div class="conditions">
    <p><span class="highlight">Conditions</span> and symptoms that<br>may <span class="highlight">benefit</span> from natural health:</p>
    <ul class="conditions-list">
      <li>hormone imbalances</li>
      <li>digestion issues</li>
      <li>kidney disorders</li>
      <li>chronic health conditions</li>
    </ul>
  </div>

  <div class="contact-bar">Call <strong>555-014-2661</strong> or visit <strong>www.marigold-health.example</strong> for more information</div>
</section>

</body>
</html>
```